Home Page Design

Please see design brief attached. Concept here: mockboard[dot]net/file/qr83TpLM5wnePxHbUoKVsY/Velvetcourse---Landing-Page?node-id=0%3A1&t=KPwq7ZnRb2xTcVuM-1

Industry/Entity Type

Wedding

Number of Pages Required

1 page

Font styles to use
Serif
Sans Serif
Decorative
Script

Colors
A7469A
B969AE
D3A5CF
EDDBEB
F8F0F9
6B429C
8869AF
B7A5CE
E3DAEB
F3F0F8

Requirements
Must have
• Please see attached PDF
Nice to have
• Please see attached PDF
Should not have
• Please see attached PDF

```html
<!DOCTYPE html>
<html lang="en">
<head>
<meta charset="utf-8">
<title>Velvetcourse – Wedding Planning</title>
<link rel="stylesheet" href="https://fonts.googleapis.com/css2?family=Nunito+Sans:wght@300;400;600;700;800&display=swap">
<style>
:root{
  --plum:#A7469A;
  --plum-soft:#B969AE;
  --plum-pale:#D3A5CF;
  --plum-mist:#EDDBEB;
  --plum-wash:#F8F0F9;
  --violet:#6B429C;
  --violet-soft:#8869AF;
  --violet-pale:#B7A5CE;
  --violet-mist:#E3DAEB;
  --violet-wash:#F3F0F8;
  --ink:#2b2430;
  --grey:#6f6a73;
  --line:#e7dfe8;
  --footer:#86307b;
  --gold:#f2b632;
}
*{box-sizing:border-box;margin:0;padding:0}
html,body{width:1200px;height:5344px;overflow:hidden}
body{font-family:"Nunito Sans",Arial,sans-serif;color:var(--ink);background:#fff;position:relative}
section,header,footer{position:absolute;left:0;width:1200px}
.btn{display:inline-block;background:var(--plum);color:#fff;border-radius:20px;font-weight:700;text-transform:uppercase;letter-spacing:.5px}
.stars{color:var(--gold);font-size:13px;letter-spacing:1px}
.section-title{position:absolute;left:0;width:1200px;text-align:center;font-size:36px;font-weight:400;color:var(--ink)}
.section-title b{font-weight:800}
.divider{position:absolute;left:540px;width:120px;height:24px}

/* hero */
.hero{top:0;height:712px;overflow:hidden}
.hero-photo{position:absolute;inset:0;background:linear-gradient(100deg,#c9b3a4 0%,#e9dcd2 30%,#d8c6c8 55%,#b89a8e 80%,#8f7367 100%)}
.hero-tint{position:absolute;left:250px;top:330px;width:700px;height:340px;background:radial-gradient(ellipse at center,rgba(167,70,154,.55) 0%,rgba(167,70,154,.2) 60%,rgba(167,70,154,0) 75%)}
.hero-nav{position:absolute;right:0;top:0;width:190px;height:28px;background:var(--violet);display:flex;justify-content:space-around;align-items:center;color:#fff;font-size:13px;font-weight:600}
.brand{position:absolute;left:0;top:42px;width:1200px;display:flex;justify-content:center;align-items:center;gap:10px;color:#fff;font-size:24px;font-weight:700}
.brand i{width:16px;height:16px;border-radius:50%;background:#fff;display:block}
.hero-kicker{position:absolute;top:378px;width:1200px;text-align:center;color:#fff;font-size:22px;font-weight:600;line-height:28px}
.hero-title{position:absolute;top:432px;width:1200px;text-align:center;color:#fff;font-size:58px;line-height:62px;font-weight:800}
.hero .btn{position:absolute;left:540px;top:606px;width:120px;height:36px;line-height:36px;text-align:center;font-size:14px}

/* stats */
.stats{top:712px;height:248px;background:var(--plum-wash);display:flex;justify-content:space-around;align-items:center;padding:0 40px}
.stat{text-align:center;width:180px}
.stat strong{display:block;font-size:40px;font-weight:600;color:var(--ink)}
.stat span{font-size:22px;color:var(--plum)}
.stat-flourish{width:90px;height:140px;background:radial-gradient(ellipse,rgba(167,70,154,.22),rgba(167,70,154,0) 70%)}

/* categories */
.categories{top:960px;height:700px}
.cat-cards{position:absolute;left:51px;top:160px;display:flex;gap:14px}
.cat{width:264px}
.cat-card{background:#fff;border-radius:8px;box-shadow:0 4px 16px rgba(80,40,80,.14);overflow:hidden;height:420px}
.cat-tab{background:var(--plum);color:#fff;text-align:center;font-size:16px;font-weight:700;height:30px;line-height:30px}
.cat-photo{height:136px}
.cat-body{padding:12px 16px;font-size:12px;color:var(--grey);position:relative}
.cat-rating{display:flex;flex-direction:column;gap:2px}
.heart{position:absolute;right:16px;top:14px;width:20px;height:18px}
.cat-body h3{font-size:20px;color:var(--ink);margin-top:10px;font-weight:700}
.loc{display:flex;align-items:center;gap:4px;margin:4px 0 8px}
.cat-body p{line-height:16px}
.price{color:var(--plum);margin:8px 0 12px;font-weight:600}
.cat-body .btn{font-size:12px;padding:6px 20px}
.more{display:flex;justify-content:center;align-items:center;gap:10px;margin-top:26px;color:var(--plum);font-size:14px;font-weight:600}
.slider-arrow{position:absolute;top:320px;width:36px;height:36px;border-radius:50%;background:var(--plum);display:flex;align-items:center;justify-content:center}

/* insured */
.insured{top:1680px;height:780px}
.insured-photo{position:absolute;left:0;top:0;width:1200px;height:680px;background:linear-gradient(110deg,#7e6a5e 0%,#bda99a 35%,#e8ddd4 55%,#b79f8c 78%,#6d5a4e 100%)}
.play{position:absolute;left:566px;top:262px;width:68px;height:68px;border-radius:50%;background:var(--plum)}
.insured-banner{position:absolute;left:60px;top:540px;width:1080px;height:230px;border-radius:22px;background:linear-gradient(90deg,var(--plum) 0%,var(--violet-soft) 100%);color:#fff;text-align:center;padding-top:80px}
.insured-banner h2{font-size:34px;font-weight:400;line-height:40px}
.insured-banner h2 b{font-weight:800}
.insured-banner p{font-size:14px;line-height:20px;margin-top:10px}
.badge{position:absolute;left:540px;top:460px;width:120px;height:120px;border-radius:50%;background:#fff;border:4px solid var(--plum);display:flex;align-items:center;justify-content:center}

/* how it works */
.how{top:2520px;height:460px}
.steps{position:absolute;left:140px;top:160px;width:920px;display:flex;justify-content:space-between}
.step{width:280px;text-align:center}
.step-icon{width:84px;height:84px;margin:0 auto;border-radius:50%;background:var(--plum-wash);display:flex;align-items:center;justify-content:center}
.step h3{font-size:17px;font-weight:700;margin:26px 0 14px;line-height:22px;min-height:44px;display:flex;align-items:center;justify-content:center}
.step p{font-size:15px;color:var(--grey);line-height:20px}

/* marketplace */
.market{top:3000px;height:700px;background:linear-gradient(180deg,var(--plum-wash) 0%,#fff 100%)}
.market-lead{position:absolute;top:152px;width:1200px;text-align:center;font-size:15px;line-height:22px}
.market-lead em{font-style:normal;color:var(--plum);display:block}
.vendor-grid{position:absolute;left:72px;top:250px;width:1056px;display:grid;grid-template-columns:repeat(5,176px);column-gap:44px;row-gap:30px}
.vendor{height:180px;background:#fff;border-radius:10px;box-shadow:0 3px 14px rgba(80,40,80,.12);display:flex;flex-direction:column;align-items:center;justify-content:center;text-align:center;gap:6px;font-size:11px;color:var(--grey)}
.vendor h4{font-size:17px;font-weight:700;color:var(--ink);line-height:20px}
.vendor.is-active{border:2px solid var(--plum)}
.vendor .btn{font-size:10px;padding:4px 14px}
.vendor svg{width:48px;height:44px}

/* testimonials */
.clients{top:3700px;height:760px}
.quotes{position:absolute;left:72px;top:260px;display:flex;gap:36px}
.quote{width:328px}
.quote-card{background:#fff;border-radius:8px;box-shadow:0 4px 18px rgba(80,40,80,.12);padding:22px 24px;height:290px}
.quote-card h4{font-size:17px;font-weight:700}
.quote-card p{font-size:15px;line-height:22px;color:var(--grey);margin-top:10px}
.client{display:flex;align-items:center;gap:14px;margin:40px 0 0 18px}
.avatar{width:56px;height:56px;border-radius:50%;background:linear-gradient(135deg,#c9a99a,#8d6e62)}
.client b{display:block;color:var(--plum);font-size:15px}
.client span{font-size:12px;color:var(--grey)}

/* newsletter */
.newsletter{top:4460px;height:400px}
.newsletter p{position:absolute;top:156px;width:1200px;text-align:center;font-size:15px;line-height:22px;color:var(--grey)}
.signup{position:absolute;left:380px;top:242px;width:440px;height:40px;border-bottom:1px solid var(--plum-pale);display:flex;justify-content:space-between;align-items:center;padding-left:40px}
.signup span{font-size:13px;color:var(--grey)}
.signup .btn{font-size:13px;padding:9px 26px}

/* footer */
.site-footer{top:4860px;height:484px;background:var(--footer);color:#fff}
.foot-cols{position:absolute;left:60px;top:36px;display:flex;gap:0}
.foot-col{width:275px}
.foot-col h5{font-size:15px;font-weight:700;margin-bottom:14px}
.foot-col li{list-style:none;font-size:10.5px;line-height:13.6px;padding-left:10px;position:relative;opacity:.92}
.foot-col li::before{content:"";position:absolute;left:0;top:6px;width:3px;height:3px;border-radius:50%;background:#fff}
.legal{position:absolute;left:60px;top:420px;width:1080px;border-top:1px solid rgba(255,255,255,.3);text-align:center;padding-top:16px;font-size:11px;opacity:.85}
</style>
</head>
<body>

<header class="hero">
  <div class="hero-photo" role="img" aria-label="Photograph of a smiling bride and groom beneath a floral arch"></div>
  <div class="hero-tint"></div>
  <nav class="hero-nav"><span>Sign Up</span><span>Login</span></nav>
  <div class="brand"><i></i>Velvetcourse</div>
  <div class="hero-kicker">Velvetcourse</div>
  <h1 class="hero-title">Be the Couple who<br>stuck to their budget!</h1>
  <a class="btn">Explore</a>
</header>

<section class="stats">
  <div class="stat"><strong>700</strong><span>Happy Couples</span></div>
  <div class="stat-flourish" role="img" aria-label="Floral flourish"></div>
  <div class="stat"><strong>1500</strong><span>Decoration</span></div>
  <div class="stat-flourish" role="img" aria-label="Floral flourish"></div>
  <div class="stat"><strong>500</strong><span>Weddings</span></div>
  <div class="stat-flourish" role="img" aria-label="Floral flourish"></div>
  <div class="stat"><strong>$7,680</strong><span>Location</span></div>
</section>

<section class="categories">
  <svg class="divider" style="top:76px" viewBox="0 0 120 24"><line x1="0" y1="12" x2="48" y2="12" stroke="#A7469A"/><line x1="72" y1="12" x2="120" y2="12" stroke="#A7469A"/><circle cx="60" cy="12" r="6" fill="none" stroke="#A7469A" stroke-width="1.5"/></svg>
  <h2 class="section-title" style="top:92px">Popular Wedding <b>Categories</b></h2>
  <div class="slider-arrow" style="left:32px"><svg width="14" height="14" viewBox="0 0 14 14"><path d="M9 2 4 7l5 5" fill="none" stroke="#fff" stroke-width="2"/></svg></div>
  <div class="slider-arrow" style="right:32px"><svg width="14" height="14" viewBox="0 0 14 14"><path d="M5 2l5 5-5 5" fill="none" stroke="#fff" stroke-width="2"/></svg></div>
  <div class="cat-cards">
    <div class="cat">
      <div class="cat-card">
        <div class="cat-tab">Venues</div>
        <div class="cat-photo" role="img" aria-label="Photograph of a wedding venue with floral arch" style="background:linear-gradient(135deg,#c5b59a,#8c9a7a)"></div>
        <div class="cat-body">
          <div class="cat-rating"><span class="stars">★★★★★</span><span>4.5 - 27 Reviews</span></div>
          <svg class="heart" viewBox="0 0 20 18"><path d="M10 16S2 11 2 6a4 4 0 0 1 8-1 4 4 0 0 1 8 1c0 5-8 10-8 10z" fill="none" stroke="#6f6a73" stroke-width="1.5"/></svg>
          <h3>Floral Graden</h3>
          <div class="loc"><svg width="10" height="12" viewBox="0 0 10 12"><path d="M5 11S1 7 1 4.5a4 4 0 0 1 8 0C9 7 5 11 5 11z" fill="#A7469A"/></svg>Location, city Address</div>
          <p>Lorem Ipsum has been the industry's standard dummy text ever since</p>
          <div class="price">Starting Price $4,000</div>
          <a class="btn">Reserve</a>
        </div>
      </div>
      <div class="more">More Venues <svg width="20" height="10" viewBox="0 0 20 10"><path d="M0 5h18M14 1l4 4-4 4" fill="none" stroke="#A7469A" stroke-width="1.5"/></svg></div>
    </div>
    <div class="cat">
      <div class="cat-card">
        <div class="cat-tab">Photographer</div>
        <div class="cat-photo" role="img" aria-label="Photograph of a wedding photographer at work" style="background:linear-gradient(135deg,#9a8f88,#d8d0c8)"></div>
        <div class="cat-body">
          <div class="cat-rating"><span class="stars">★★★★★</span><span>4.5 - 27 Reviews</span></div>
          <svg class="heart" viewBox="0 0 20 18"><path d="M10 16S2 11 2 6a4 4 0 0 1 8-1 4 4 0 0 1 8 1c0 5-8 10-8 10z" fill="none" stroke="#6f6a73" stroke-width="1.5"/></svg>
          <h3>Floral Graden</h3>
          <div class="loc"><svg width="10" height="12" viewBox="0 0 10 12"><path d="M5 11S1 7 1 4.5a4 4 0 0 1 8 0C9 7 5 11 5 11z" fill="#A7469A"/></svg>Location, city Address</div>
          <p>Lorem Ipsum has been the industry's standard dummy text ever since</p>
          <div class="price">Starting Price $4,000</div>
          <a class="btn">Reserve</a>
        </div>
      </div>
      <div class="more">More Photographer <svg width="20" height="10" viewBox="0 0 20 10"><path d="M0 5h18M14 1l4 4-4 4" fill="none" stroke="#A7469A" stroke-width="1.5"/></svg></div>
    </div>
    <div class="cat">
      <div class="cat-card">
        <div class="cat-tab">Cake</div>
        <div class="cat-photo" role="img" aria-label="Photograph of a tiered white wedding cake" style="background:linear-gradient(135deg,#ece6df,#bfb2a6)"></div>
        <div class="cat-body">
          <div class="cat-rating"><span class="stars">★★★★★</span><span>4.5 - 27 Reviews</span></div>
          <svg class="heart" viewBox="0 0 20 18"><path d="M10 16S2 11 2 6a4 4 0 0 1 8-1 4 4 0 0 1 8 1c0 5-8 10-8 10z" fill="none" stroke="#6f6a73" stroke-width="1.5"/></svg>
          <h3>Floral Graden</h3>
          <div class="loc"><svg width="10" height="12" viewBox="0 0 10 12"><path d="M5 11S1 7 1 4.5a4 4 0 0 1 8 0C9 7 5 11 5 11z" fill="#A7469A"/></svg>Location, city Address</div>
          <p>Lorem Ipsum has been the industry's standard dummy text ever since</p>
          <div class="price">Starting Price $4,000</div>
          <a class="btn">Reserve</a>
        </div>
      </div>
      <div class="more">More Catering <svg width="20" height="10" viewBox="0 0 20 10"><path d="M0 5h18M14 1l4 4-4 4" fill="none" stroke="#A7469A" stroke-width="1.5"/></svg></div>
    </div>
    <div class="cat">
      <div class="cat-card">
        <div class="cat-tab">Event Planning</div>
        <div class="cat-photo" role="img" aria-label="Photograph of a decorated wedding reception" style="background:linear-gradient(135deg,#d6c3b4,#9b7f70)"></div>
        <div class="cat-body">
          <div class="cat-rating"><span class="stars">★★★★★</span><span>4.5 - 27 Reviews</span></div>
          <svg class="heart" viewBox="0 0 20 18"><path d="M10 16S2 11 2 6a4 4 0 0 1 8-1 4 4 0 0 1 8 1c0 5-8 10-8 10z" fill="none" stroke="#6f6a73" stroke-width="1.5"/></svg>
          <h3>Floral Graden</h3>
          <div class="loc"><svg width="10" height="12" viewBox="0 0 10 12"><path d="M5 11S1 7 1 4.5a4 4 0 0 1 8 0C9 7 5 11 5 11z" fill="#A7469A"/></svg>Location, city Address</div>
          <p>Lorem Ipsum has been the industry's standard dummy text ever since</p>
          <div class="price">Starting Price $4,000</div>
          <a class="btn">Reserve</a>
        </div>
      </div>
      <div class="more">More Planning <svg width="20" height="10" viewBox="0 0 20 10"><path d="M0 5h18M14 1l4 4-4 4" fill="none" stroke="#A7469A" stroke-width="1.5"/></svg></div>
    </div>
  </div>
</section>

<section class="insured">
  <div class="insured-photo" role="img" aria-label="Photograph of a couple sitting together on a beach at their wedding"></div>
  <div class="play"><svg width="68" height="68" viewBox="0 0 68 68"><path d="M28 22v24l20-12z" fill="#fff"/></svg></div>
  <div class="insured-banner">
    <h2>Velvetsure!- Because Life happens.All<br><b>Your Bookings fully insured</b></h2>
    <p>Lorem Ipsum is simply dummy text of the printing and typesetting industry. Lorem Ipsum<br>has been the industry's</p>
  </div>
  <div class="badge"><svg width="56" height="56" viewBox="0 0 56 56"><path d="M28 6 46 13v14c0 12-8 20-18 23C18 47 10 39 10 27V13z" fill="none" stroke="#A7469A" stroke-width="2.5"/><path d="M20 28l6 6 11-12" fill="none" stroke="#A7469A" stroke-width="2.5"/></svg></div>
</section>

<section class="how">
  <svg class="divider" style="top:40px" viewBox="0 0 120 24"><line x1="0" y1="12" x2="48" y2="12" stroke="#A7469A"/><line x1="72" y1="12" x2="120" y2="12" stroke="#A7469A"/><circle cx="60" cy="12" r="6" fill="none" stroke="#A7469A" stroke-width="1.5"/></svg>
  <h2 class="section-title" style="top:70px">How It <b>Works</b></h2>
  <div class="steps">
    <div class="step">
      <div class="step-icon"><svg width="44" height="44" viewBox="0 0 44 44"><rect x="4" y="8" width="36" height="26" rx="3" fill="none" stroke="#2b2430" stroke-width="2"/><circle cx="22" cy="21" r="6" fill="none" stroke="#A7469A" stroke-width="2"/><line x1="14" y1="40" x2="30" y2="40" stroke="#2b2430" stroke-width="2"/></svg></div>
      <h3>Browse Top Vendors</h3>
      <p>Lorem Ipsum is simply dummy text of the printing and typesetting industry. Lorem Ipsum hasbeen the industry's</p>
    </div>
    <div class="step">
      <div class="step-icon"><svg width="44" height="44" viewBox="0 0 44 44"><rect x="6" y="8" width="32" height="30" rx="3" fill="none" stroke="#2b2430" stroke-width="2"/><line x1="6" y1="16" x2="38" y2="16" stroke="#2b2430" stroke-width="2"/><path d="M15 27l5 5 9-9" fill="none" stroke="#A7469A" stroke-width="2"/></svg></div>
      <h3>Instantly Book With<br>Pre-negotiated Prices</h3>
      <p>Lorem Ipsum is simply dummy text of the printing and typesetting industry. Lorem Ipsum hasbeen the industry's</p>
    </div>
    <div class="step">
      <div class="step-icon"><svg width="44" height="44" viewBox="0 0 44 44"><rect x="10" y="4" width="24" height="36" rx="3" fill="none" stroke="#2b2430" stroke-width="2"/><text x="22" y="27" text-anchor="middle" font-size="14" font-weight="700" fill="#A7469A" font-family="Nunito Sans, sans-serif">$</text></svg></div>
      <h3>Pay Over Time</h3>
      <p>Lorem Ipsum is simply dummy text of the printing and typesetting industry. Lorem Ipsum hasbeen the industry's</p>
    </div>
  </div>
</section>

<section class="market">
  <svg class="divider" style="top:72px" viewBox="0 0 120 24"><line x1="0" y1="12" x2="48" y2="12" stroke="#A7469A"/><line x1="72" y1="12" x2="120" y2="12" stroke="#A7469A"/><circle cx="60" cy="12" r="6" fill="none" stroke="#A7469A" stroke-width="1.5"/></svg>
  <h2 class="section-title" style="top:98px">Explore <b>The Marketplace</b></h2>
  <div class="market-lead"><em>Because life is too short to wait for vendors to reply.</em>Focus on enjoying your wedding! Don't get tied into endless negotiations and emails.</div>
  <div class="vendor-grid">
    <div class="vendor is-active"><svg viewBox="0 0 48 44"><path d="M4 20 24 6l20 14M8 18v22h32V18" fill="none" stroke="#2b2430" stroke-width="2"/><rect x="19" y="26" width="10" height="14" fill="none" stroke="#A7469A" stroke-width="2"/></svg><h4>Venues</h4><span><span class="stars">★★★★★</span> 4.5 - 27 Reviews</span><a class="btn">Reserve</a></div>
    <div class="vendor"><svg viewBox="0 0 48 44"><rect x="4" y="12" width="40" height="28" rx="3" fill="none" stroke="#2b2430" stroke-width="2"/><circle cx="24" cy="26" r="8" fill="none" stroke="#A7469A" stroke-width="2"/><path d="M16 12l3-6h10l3 6" fill="none" stroke="#2b2430" stroke-width="2"/></svg><h4>Photographer</h4><span><span class="stars">★★★★★</span> 4.5 - 27 Reviews</span></div>
    <div class="vendor"><svg viewBox="0 0 48 44"><path d="M6 32a18 18 0 0 1 36 0z" fill="none" stroke="#2b2430" stroke-width="2"/><line x1="2" y1="36" x2="46" y2="36" stroke="#A7469A" stroke-width="2"/><circle cx="24" cy="12" r="2" fill="#2b2430"/></svg><h4>Caterers</h4><span><span class="stars">★★★★★</span> 4.5 - 27 Reviews</span></div>
    <div class="vendor"><svg viewBox="0 0 48 44"><circle cx="24" cy="14" r="9" fill="none" stroke="#A7469A" stroke-width="2"/><path d="M24 23v18M16 32l8 6 8-6" fill="none" stroke="#2b2430" stroke-width="2"/></svg><h4>Florists</h4><span><span class="stars">★★★★★</span> 4.5 - 27 Reviews</span></div>
    <div class="vendor"><svg viewBox="0 0 48 44"><path d="M10 6h12l-2 14a4 4 0 0 1-8 0zM16 24v14M11 40h10" fill="none" stroke="#2b2430" stroke-width="2"/><path d="M28 10h12l-2 12a4 4 0 0 1-8 0zM34 26v12M29 40h10" fill="none" stroke="#A7469A" stroke-width="2"/></svg><h4>Bar &amp; Beverages</h4><span><span class="stars">★★★★★</span> 4.5 - 27 Reviews</span></div>
    <div class="vendor"><svg viewBox="0 0 48 44"><circle cx="24" cy="16" r="10" fill="none" stroke="#2b2430" stroke-width="2"/><path d="M8 42c2-9 8-13 16-13s14 4 16 13" fill="none" stroke="#A7469A" stroke-width="2"/></svg><h4>Beauty<br>Professionals</h4><span><span class="stars">★★★★★</span> 4.5 - 27 Reviews</span></div>
    <div class="vendor"><svg viewBox="0 0 48 44"><rect x="8" y="4" width="32" height="36" rx="3" fill="none" stroke="#2b2430" stroke-width="2"/><line x1="15" y1="14" x2="33" y2="14" stroke="#A7469A" stroke-width="2"/><line x1="15" y1="22" x2="33" y2="22" stroke="#A7469A" stroke-width="2"/><line x1="15" y1="30" x2="27" y2="30" stroke="#A7469A" stroke-width="2"/></svg><h4>Planners</h4><span><span class="stars">★★★★★</span> 4.5 - 27 Reviews</span></div>
    <div class="vendor"><svg viewBox="0 0 48 44"><path d="M18 34V8l20-4v26" fill="none" stroke="#2b2430" stroke-width="2"/><circle cx="13" cy="34" r="5" fill="none" stroke="#A7469A" stroke-width="2"/><circle cx="33" cy="30" r="5" fill="none" stroke="#A7469A" stroke-width="2"/></svg><h4>Bands and DJs</h4><span><span class="stars">★★★★★</span> 4.5 - 27 Reviews</span></div>
    <div class="vendor"><svg viewBox="0 0 48 44"><rect x="8" y="26" width="32" height="14" fill="none" stroke="#2b2430" stroke-width="2"/><rect x="14" y="14" width="20" height="12" fill="none" stroke="#A7469A" stroke-width="2"/><line x1="24" y1="4" x2="24" y2="14" stroke="#2b2430" stroke-width="2"/></svg><h4>Cake And Dessert</h4><span><span class="stars">★★★★★</span> 4.5 - 27 Reviews</span></div>
    <div class="vendor"><svg viewBox="0 0 48 44"><rect x="4" y="12" width="28" height="22" rx="3" fill="none" stroke="#2b2430" stroke-width="2"/><path d="M32 20l12-6v18l-12-6" fill="none" stroke="#A7469A" stroke-width="2"/></svg><h4>Videographers</h4><span><span class="stars">★★★★★</span> 4.5 - 27 Reviews</span></div>
  </div>
</section>

<section class="clients">
  <svg class="divider" style="top:64px" viewBox="0 0 120 24"><line x1="0" y1="12" x2="48" y2="12" stroke="#A7469A"/><line x1="72" y1="12" x2="120" y2="12" stroke="#A7469A"/><circle cx="60" cy="12" r="6" fill="none" stroke="#A7469A" stroke-width="1.5"/></svg>
  <h2 class="section-title" style="top:90px">What our <b>Clients are saying</b></h2>
  <div class="quotes">
    <div class="quote">
      <div class="quote-card"><h4>Wedding Hashtag</h4><span class="stars">★★★★★</span><p>Lorem Ipsum is simply dummy text of the printing and typesetting industry. Lorem Ipsum has been the industry's standard dummy text ever since the, when an this unknown printer took a galley.</p></div>
      <div class="client"><div class="avatar" role="img" aria-label="Client portrait"></div><div><b>Client Name</b><span>17 dec , 2022</span></div></div>
    </div>
    <div class="quote">
      <div class="quote-card"><h4>Wedding Hashtag</h4><span class="stars">★★★★★</span><p>Lorem Ipsum is simply dummy text of the printing and typesetting industry. Lorem Ipsum has been the industry's standard dummy text ever since the, when an this unknown printer took a galley.</p></div>
      <div class="client"><div class="avatar" role="img" aria-label="Client portrait"></div><div><b>Client Name</b><span>17 dec , 2022</span></div></div>
    </div>
    <div class="quote">
      <div class="quote-card"><h4>Wedding Hashtag</h4><span class="stars">★★★★★</span><p>Lorem Ipsum is simply dummy text of the printing and typesetting industry. Lorem Ipsum has been the industry's standard dummy text ever since the, when an this unknown printer took a galley.</p></div>
      <div class="client"><div class="avatar" role="img" aria-label="Client portrait"></div><div><b>Client Name</b><span>17 dec , 2022</span></div></div>
    </div>
  </div>
</section>

<section class="newsletter">
  <svg class="divider" style="top:52px" viewBox="0 0 120 24"><line x1="0" y1="12" x2="48" y2="12" stroke="#A7469A"/><line x1="72" y1="12" x2="120" y2="12" stroke="#A7469A"/><circle cx="60" cy="12" r="6" fill="none" stroke="#A7469A" stroke-width="1.5"/></svg>
  <h2 class="section-title" style="top:88px">Subscribe To Our <b>Newsletter</b></h2>
  <p>Lorem Ipsum is simply dummy text of the printing and typesetting industry. Lorem<br>Ipsum has been the industry's</p>
  <div class="signup"><span>E-mail</span><a class="btn">Get Start</a></div>
</section>

<footer class="site-footer">
  <div class="foot-cols">
    <div class="foot-col">
      <h5>Local Services</h5>
      <ul>
        <li>Wedding Photographers</li><li>Wedding DJs</li><li>Wedding Hair &amp; Makeup</li><li>Wedding Planners</li><li>Wedding Florists</li><li>Wedding Caterers</li><li>Wedding Videographers</li><li>Wedding Officiants</li><li>Wedding Rentals</li><li>Wedding Photo Booths</li><li>Wedding Bands</li><li>Wedding Dresses &amp; Attire</li><li>Wedding Cakes</li><li>Wedding Limos / Transportation</li><li>Wedding Musicians / Ceremony Music</li><li>Wedding Decor &amp; Lighting</li><li>Travel Agents</li><li>Wedding Jewelers</li><li>Wedding Favors &amp; Gifts</li><li>Day Of Wedding Coordinators</li><li>Wedding Dance Lessons</li>
      </ul>
    </div>
    <div class="foot-col">
      <h5>Digital Services</h5>
      <ul>
        <li>Logo Design</li><li>Pictures &amp; Caricatures</li><li>Video Editing</li><li>Invitation Design</li><li>Image Editing</li><li>Slideshow Videos</li><li>Speech Writing</li><li>Wedding Cards &amp; Videos</li>
      </ul>
    </div>
    <div class="foot-col">
      <h5>Support</h5>
      <ul>
        <li>Help &amp; Support</li><li>Trust &amp; Safety</li><li>Selling On Velvetcourse</li><li>Buying on Velvetcourse</li>
      </ul>
    </div>
    <div class="foot-col">
      <h5>More from Velvetcourse</h5>
      <ul>
        <li>Velvetcourse Business</li><li>Velvetcourse Pro</li><li>Careers</li><li>Press &amp; News</li><li>Partnerships</li><li>Privacy Policy</li><li>Terms of Service</li>
      </ul>
    </div>
  </div>
  <div class="legal">© 2022 Wedding Velvetcourse . All rights reserved.</div>
</footer>

</body>
</html>
```